Carton Box Packaging For Motorcycle Brake Shoe - Vorenta Brand

Packaging Dimensions: 125mm (H) x 125mm (W) x 31mm (D)
We would like to design a genuine Carton box Packaging for motorcycle Brake Shoe.
This is a critical part of the motorcycle, so we need the packaging to reflect elegant impression.
Vorenta, is one of the leading companies for manufacturing Motorcycles, located in Egypt. Our company is offering high-quality products, the best in the local market, with very competitive prices.
We have a limited time to get this project done, So we Highly appreciate receiving your designs ASAP.
Target Market(s)
Economical Motorcycle Buyers
Font styles to use
Colors
Designer to choose colors to be used in the design.
Look and feel
Each slider illustrates characteristics of the customer's brand and the style your logo design should communicate.

```html
<!DOCTYPE html>
<html lang="en">
<head>
<meta charset="utf-8">
<title>Vorenta Motorcycle Brake Shoe Carton</title>
<link rel="stylesheet" href="https://fonts.googleapis.com/css2?family=Russo+One&family=Exo+2:wght@500;600;700&display=swap">
<style>
  :root {
    --page: #ececec;
    --navy: #0b1430;
    --blue: #0a63c9;
    --blue-bright: #1684e6;
    --red: #d0182a;
    --black: #0a0a0c;
    --silver: #e8e8ea;
    --white: #ffffff;
  }
  * { box-sizing: border-box; margin: 0; padding: 0; }
  html, body { width: 1200px; height: 801px; overflow: hidden; background: var(--page); }
  body { position: relative; font-family: "Exo 2", sans-serif; }

  /* Side (spine) panel */
  .side-panel {
    position: absolute; left: 134px; top: 8px; width: 150px; height: 620px;
    overflow: hidden;
    background: linear-gradient(180deg, var(--blue-bright) 0%, var(--blue) 55%, #06284f 80%, var(--black) 100%);
    display: flex; flex-direction: column; align-items: center; padding-top: 34px; gap: 30px;
  }
  .side-brand {
    display: flex; flex-direction: column; align-items: center; gap: 10px;
    font-family: "Russo One", sans-serif; font-size: 20px; color: var(--silver); letter-spacing: 2px;
  }
  .side-brand .brand-dot { width: 28px; height: 28px; border-radius: 50%; background: var(--silver); }
  .side-brand .name { writing-mode: vertical-rl; }
  .side-title {
    writing-mode: vertical-rl; font-family: "Russo One", sans-serif; color: var(--silver);
    line-height: .95; white-space: nowrap;
  }
  .side-title .kicker { font-size: 18px; letter-spacing: 3px; }
  .side-title .main { font-size: 50px; letter-spacing: 1px; }
  .side-title .genuine-small {
    display: inline-block; margin-top: 130px; padding: 6px 3px;
    border: 1.5px solid var(--silver); font-size: 11px; letter-spacing: 2px;
  }

  /* Top panel */
  .top-panel {
    position: absolute; left: 290px; top: 8px; width: 620px; height: 620px;
    overflow: hidden; background: var(--navy);
  }
  .top-panel .swoosh { position: absolute; inset: 0; }

  .brand {
    position: absolute; left: 40px; top: 40px;
    display: flex; align-items: center; gap: 12px;
    font-family: "Russo One", sans-serif; font-size: 26px; color: var(--silver);
    letter-spacing: 2px;
  }
  .brand-dot { width: 34px; height: 34px; border-radius: 50%; background: var(--silver); }

  .title { position: absolute; left: 230px; top: 70px; font-family: "Russo One", sans-serif; color: var(--silver); line-height: .9; font-weight: 400; }
  .title .kicker { font-size: 30px; letter-spacing: 4px; }
  .title .main { font-size: 104px; letter-spacing: 2px; }
  .title .main.second { padding-left: 70px; }
  .genuine {
    display: inline-block; margin: 8px 0 0 140px; padding: 4px 12px;
    border: 2px solid var(--silver); font-size: 18px; letter-spacing: 3px; white-space: nowrap;
  }

  .product-photo {
    position: absolute; left: 60px; top: 270px; width: 270px; height: 170px;
    border-radius: 80px;
    background: radial-gradient(ellipse at 40% 40%, #f1f1f1 0%, #b9b9bb 45%, #8b6f52 75%, #5a4330 100%);
  }

  .benefit-band {
    position: absolute; left: 250px; top: 330px; width: 370px; height: 36px;
    background: linear-gradient(90deg, rgba(208,24,42,0) 0%, var(--red) 22%, var(--red) 100%);
    color: var(--white); font-size: 10px; font-weight: 600; letter-spacing: 1.2px;
    display: flex; align-items: center; justify-content: flex-end; padding-right: 18px;
    white-space: nowrap;
  }

  .info-row {
    position: absolute; left: 345px; top: 388px; width: 255px;
    display: flex; justify-content: space-between; gap: 20px; color: var(--white);
    font-size: 12px; font-weight: 600; letter-spacing: 1.5px; white-space: nowrap;
  }

  .asbestos {
    position: absolute; left: 150px; top: 458px; color: var(--white);
    font-size: 24px; font-weight: 600; letter-spacing: 1px; display: flex; align-items: center; gap: 10px;
    white-space: nowrap;
  }

  .handling {
    position: absolute; left: 500px; top: 455px;
    display: grid; grid-template-columns: 44px 44px; gap: 6px;
  }
  .handling svg { width: 44px; height: 44px; border: 1.5px solid var(--silver); }

  /* Front panel */
  .front-panel {
    position: absolute; left: 290px; top: 634px; width: 620px; height: 156px;
    background: var(--black); overflow: hidden;
    display: flex; align-items: center; justify-content: center;
  }
  .front-panel .edge { position: absolute; left: 0; top: 0; width: 180px; height: 100%; background: linear-gradient(90deg, var(--blue) 0%, rgba(10,99,201,0) 100%); }
  .front-title { position: relative; font-family: "Russo One", sans-serif; color: var(--silver); line-height: .9; }
  .front-title .kicker { font-size: 18px; letter-spacing: 3px; }
  .front-title .main { font-size: 58px; letter-spacing: 1px; white-space: nowrap; }
  .front-title .genuine { margin-left: 210px; font-size: 12px; margin-top: 4px; padding: 2px 8px; }
</style>
</head>
<body>
  <aside class="side-panel">
    <div class="side-brand"><span class="brand-dot"></span><span class="name">VORENTA</span></div>
    <div class="side-title">
      <div class="kicker">MOTORCYCLE</div>
      <div class="main">BRAKE SHOE</div>
      <div class="genuine-small">GENUINE PARTS</div>
    </div>
  </aside>

  <section class="top-panel">
    <svg class="swoosh" viewBox="0 0 620 620" preserveAspectRatio="none" aria-hidden="true">
      <defs>
        <linearGradient id="blueSide" x1="0" y1="0" x2="1" y2="0">
          <stop offset="0" stop-color="#1684e6"/><stop offset="1" stop-color="#0a4fb0"/>
        </linearGradient>
        <linearGradient id="redArc" x1="0" y1="0" x2="1" y2="0">
          <stop offset="0" stop-color="#d0182a"/><stop offset="1" stop-color="#3b1a5a"/>
        </linearGradient>
      </defs>
      <rect width="620" height="620" fill="#0b1430"/>
      <path d="M0 0 H360 C240 80 170 220 170 360 C170 470 210 560 260 620 H0 Z" fill="url(#blueSide)"/>
      <path d="M360 0 H420 C280 80 200 220 200 360 C200 470 230 560 280 620 H260 C210 560 170 470 170 360 C170 220 240 80 360 0 Z" fill="url(#redArc)"/>
      <path d="M0 400 H620 V620 H0 Z" fill="#0a0a0c" opacity=".85"/>
      <path d="M0 400 C60 470 120 560 240 620 H200 C100 560 40 480 0 430 Z" fill="#0a4fb0"/>
    </svg>

    <div class="brand"><span class="brand-dot"></span>VORENTA</div>

    <h1 class="title">
      <div class="kicker">MOTORCYCLE</div>
      <div class="main">BRAKE</div>
      <div class="main second">SHOE</div>
      <div class="genuine">GENUINE PARTS</div>
    </h1>

    <div class="product-photo" role="img" aria-label="Photo of a pair of motorcycle drum brake shoes with springs"></div>

    <div class="benefit-band">EXTENDED LIFE | LOW DUST | MAX STOPPING POWER</div>

    <div class="info-row"><span>www.vorenta.com</span><span>MADE IN CHAIN</span></div>

    <div class="asbestos">
      <svg width="30" height="18" viewBox="0 0 31 18" aria-hidden="true">
        <path d="M0 0 L8 9 L0 18 H5 L13 9 L5 0 Z M9 0 L17 9 L9 18 H14 L22 9 L14 0 Z M18 0 L26 9 L18 18 H23 L31 9 L23 0 Z" fill="#d0182a"/>
      </svg>
      ASBESTOS FREE
    </div>

    <div class="handling" aria-label="Handling symbols">
      <svg viewBox="0 0 44 44" aria-label="Handle with care"><rect x="16" y="10" width="12" height="10" fill="none" stroke="#e8e8ea" stroke-width="2"/><path d="M8 22 L16 32 H28 L36 22" fill="none" stroke="#e8e8ea" stroke-width="2"/></svg>
      <svg viewBox="0 0 44 44" aria-label="This way up"><path d="M15 34 V12 M10 17 L15 10 L20 17 M29 34 V12 M24 17 L29 10 L34 17 M9 36 H35" fill="none" stroke="#e8e8ea" stroke-width="2"/></svg>
      <svg viewBox="0 0 44 44" aria-label="Fragile"><path d="M14 9 H30 L28 20 C27 24 17 24 16 20 Z M22 23 V34 M15 35 H29" fill="none" stroke="#e8e8ea" stroke-width="2"/></svg>
      <svg viewBox="0 0 44 44" aria-label="Keep dry"><path d="M8 22 C10 12 34 12 36 22 Z M22 22 V33 C22 36 17 36 17 33" fill="none" stroke="#e8e8ea" stroke-width="2"/></svg>
    </div>
  </section>

  <section class="front-panel">
    <div class="edge"></div>
    <div class="front-title">
      <div class="kicker">MOTORCYCLE</div>
      <div class="main">BRAKE SHOE</div>
      <div class="genuine">GENUINE PARTS</div>
    </div>
  </section>
</body>
</html>
```